Update Old OR create new Website

Current Website is looking a bit old, I did this one a few years back.

Would like a fresh new look, current website sitepress theme is " the Vanta theme" from plumcrate and I just purchased this theme - "bravlo" also from plumcrate, I quite like the look of - http://bravlo.quorvex-skins.com/tech-business/ and if we could get somthing simlar would be great.

current website is at http://www.hle.com.au, have been playing around with the slider that i like.

I have said 5 pages to be designed but really it is just a 5 page website where most pages will look the same.

Any questions please let me know

Target Market(s)

Business

Coding

Coded - Design and coding required

Number of Pages Required

5+ page

Font styles to use
Sans Serif

Colors
33a6d7
0292cd
ffffff
0255a3

Requirements
Must have
• Device compatibility - pc, tablet, phone
Nice to have
• video
Should not have
• vunerabilities. Must also use images that will expire or disappear, ie must be uploaded to site not links to elsewhere.

```html
<!DOCTYPE html>
<html lang="en">
<head>
<meta charset="utf-8">
<title>HLE Technologies</title>
<link href="https://fonts.googleapis.com/css2?family=Lato:wght@300;400;700;900&display=swap" rel="stylesheet">
<style>
:root{
  --sky:#33a6d7;
  --blue:#0292cd;
  --navy:#0255a3;
  --deep:#0a2f5c;
  --white:#ffffff;
  --ink:#333a40;
  --muted:#8a9299;
  --line:#e3e7ea;
  --pale:#f4f6f7;
  --footer:#1f2224;
}
*{box-sizing:border-box;margin:0;padding:0}
html,body{width:1200px;height:3930px;overflow:hidden}
body{font-family:"Lato",Arial,sans-serif;color:var(--ink);background:var(--white);position:relative}
section,header,footer{position:absolute;left:0;width:1200px}
.abs{position:absolute}
.h2{font-size:30px;font-weight:400;letter-spacing:1px;text-transform:uppercase;text-align:center;color:#222}

/* header */
.site-header{top:0;height:125px;border-top:5px solid var(--sky);background:var(--white)}
.brand{left:100px;top:30px;display:flex;align-items:center;gap:12px}
.brand-mark{width:46px;height:46px;background:var(--blue)}
.brand-name{font-size:24px;font-weight:700;color:var(--navy)}
.main-nav{right:100px;top:48px;display:flex;gap:8px;align-items:center}
.main-nav a{font-size:15px;color:#555;text-decoration:none;padding:6px 12px}
.main-nav a.active{background:var(--sky);color:var(--white)}

/* hero */
.hero{top:125px;height:455px;background:radial-gradient(ellipse at 50% 40%,#1c6fa9 0%,#0d3f73 55%,#082a50 100%)}
.hero-title{top:110px;width:100%;text-align:center;color:var(--white);font-size:74px;font-weight:900;letter-spacing:2px}
.hero-sub{top:215px;width:100%;text-align:center;color:#dbe9f5;font-size:17px}
.hero-btns{top:275px;left:0;width:100%;display:flex;justify-content:center;gap:14px}
.btn{display:inline-block;font-size:14px;font-weight:700;text-transform:uppercase;padding:13px 28px;text-decoration:none}
.btn-ghost{border:2px solid var(--white);color:var(--white)}
.btn-solid{background:var(--white);color:var(--blue);border:2px solid var(--white)}
.arrow{top:195px;width:30px;height:60px}

/* about */
.about{top:580px;height:445px}
.about h2{left:100px;top:95px;font-size:30px;font-weight:400;text-transform:uppercase}
.about-text{left:100px;top:150px;width:500px;font-size:14px;line-height:28px;color:var(--muted)}
.about-text p{margin-bottom:4px}
.video{left:650px;top:75px;width:448px;height:295px;background:linear-gradient(135deg,#c9d3dc,#7d8b99 60%,#3f4a55);border:4px solid var(--white);box-shadow:0 0 0 1px var(--line)}
.play{left:838px;top:198px;width:56px;height:56px;border-radius:50%;background:#c8302b}

/* why */
.why{top:1025px;height:485px;background:var(--pale)}
.why .h2{top:75px;width:100%}
.cards{top:155px;left:100px;display:flex;gap:18px}
.card{width:238px;height:245px;background:var(--white);text-align:center;padding:28px 22px 0;box-shadow:0 1px 3px rgba(0,0,0,.06)}
.card.featured{background:var(--sky);color:var(--white)}
.card svg{width:54px;height:46px}
.card h3{font-size:16px;font-weight:400;text-transform:uppercase;margin:16px 0 10px;color:#444}
.card p{font-size:12px;line-height:20px;color:var(--muted)}
.card .more{display:block;margin-top:12px;font-size:11px;font-weight:700;color:var(--blue)}
.card.featured h3,.card.featured p,.card.featured .more{color:var(--white)}

/* services */
.services{top:1510px;height:575px}
.devices{left:120px;top:110px;width:460px;height:300px;background:linear-gradient(160deg,#dfe7ee,#9fb6c8 55%,#3b6f9a);}
.features{left:720px;top:75px;width:360px}
.feature{display:flex;gap:18px;margin-bottom:26px}
.feature svg{width:32px;height:32px;flex:none}
.feature h4{font-size:15px;font-weight:400;color:#333}
.feature p{font-size:12px;line-height:18px;color:var(--muted)}
.stores{left:738px;top:445px;display:flex;gap:10px}
.store{width:145px;height:52px;background:#111;border-radius:6px}

/* contact */
.contact{top:2085px;height:515px;background:var(--pale)}
.contact .h2{top:58px;width:100%}
.form{left:148px;top:112px;width:904px}
.field{position:absolute;height:46px;background:var(--white);border:1px solid var(--line);font-size:11px;color:#999;padding:14px 14px;text-transform:uppercase}
.send{left:455px;top:362px;width:290px;height:44px;background:var(--sky);color:var(--white);font-size:14px;text-transform:uppercase;text-align:center;line-height:44px}

/* blog */
.blog{top:2600px;height:530px}
.blog .h2{top:75px;width:100%}
.posts{top:138px;left:100px;display:flex;gap:38px}
.post{width:308px}
.post-img{height:177px;border:4px solid var(--white);box-shadow:0 0 0 1px var(--line)}
.post h3{margin-top:24px;font-size:15px;font-weight:400;text-transform:uppercase;color:#333}
.post p{font-size:12px;line-height:19px;color:var(--muted);margin-top:8px}
.post .more{display:inline-block;margin-top:20px;border:1px solid var(--sky);color:var(--blue);font-size:10px;font-weight:700;padding:5px 10px}

/* newsletter */
.newsletter{top:3130px;height:250px;background:linear-gradient(120deg,var(--navy),var(--blue) 55%,var(--sky))}
.newsletter h2{top:55px;width:100%;text-align:center;color:var(--white);font-size:26px;font-weight:400;text-transform:uppercase}
.newsletter p{top:100px;width:100%;text-align:center;color:#d7ecf7;font-size:12px}
.subscribe{left:295px;top:145px;display:flex}
.subscribe .input{width:468px;height:48px;border:1px solid rgba(255,255,255,.6);color:var(--white);font-size:13px;padding:15px 16px}
.subscribe .go{width:142px;height:48px;background:var(--white);color:var(--blue);font-weight:700;font-size:14px;text-align:center;line-height:48px}

/* partners */
.partners{top:3380px;height:160px;display:flex;justify-content:space-around;align-items:center;padding:0 110px}
.partner{display:flex;align-items:center;gap:10px;font-size:32px;font-weight:400;color:#777}
.partner i{display:block;width:30px;height:30px;background:#999}

/* footer */
.site-footer{top:3540px;height:390px;background:var(--footer);color:#ccc}
.f-brand{left:100px;top:45px;display:flex;align-items:center;gap:12px}
.f-brand .brand-name{color:var(--white);font-size:26px}
.socials{left:100px;top:160px;display:flex;gap:10px}
.socials i{width:30px;height:30px;background:#4d5357;display:block}
.col{top:45px;font-size:13px}
.col h4{color:var(--white);font-size:14px;font-weight:700;text-transform:uppercase;margin-bottom:18px}
.col ul{list-style:none;columns:2;column-gap:30px}
.col li{margin-bottom:14px}
.col li::before{content:"\25B8";color:var(--sky);margin-right:10px}
.contact-list li{display:flex;gap:12px;margin-bottom:18px;line-height:19px}
.contact-list svg{width:18px;height:18px;flex:none}
.copy{top:335px;width:100%;text-align:center;font-size:12px;color:#ddd;border-top:1px solid #2e3235;padding-top:20px}
</style>
</head>
<body>

<header class="site-header">
  <div class="abs brand"><span class="brand-mark"></span><span class="brand-name">HLE Technologies</span></div>
  <nav class="abs main-nav">
    <a class="active">Home</a><a>Servers</a><a>Networks</a><a>Managed IT</a><a>Web</a><a>App's</a><a>Internet</a><a>Contact</a>
    <svg width="18" height="18" viewBox="0 0 18 18"><circle cx="7" cy="7" r="5.5" fill="none" stroke="#33a6d7" stroke-width="2.4"/><line x1="11" y1="11" x2="16" y2="16" stroke="#33a6d7" stroke-width="2.6"/></svg>
  </nav>
</header>

<section class="hero" role="img" aria-label="Slider backdrop of glowing blue network light">
  <h1 class="abs hero-title">HLE TECHNOLOGIES</h1>
  <p class="abs hero-sub">It's this attitude that means HLE Technologies enjoys long-term relationships with its clients</p>
  <div class="abs hero-btns"><a class="btn btn-ghost">Read more</a><a class="btn btn-solid">Contact us</a></div>
  <svg class="abs arrow" style="left:40px" viewBox="0 0 30 60"><polyline points="26,4 4,30 26,56" fill="none" stroke="#fff" stroke-opacity=".7" stroke-width="2"/></svg>
  <svg class="abs arrow" style="right:40px" viewBox="0 0 30 60"><polyline points="4,4 26,30 4,56" fill="none" stroke="#fff" stroke-opacity=".7" stroke-width="2"/></svg>
</section>

<section class="about">
  <h2 class="abs">About us</h2>
  <div class="abs about-text">
    <p>What would it take for your information systems to actually improve the performance of your organisation? Through HLE Technologies, companies outsource all the expertise they need to secure their systems and optimise the output of their people and IT resources – without the expense of maintaining large internal IT departments.</p>
    <p>With a decade of experience, HLE Technologies understands the challenges faced by SMEs. So when we design and build networks, support solutions, hardware and software there's room for growth, change and mobility.</p>
  </div>
  <div class="abs video" role="img" aria-label="Video still of hands typing on a laptop"></div>
  <svg class="abs play" viewBox="0 0 56 56"><polygon points="22,17 40,28 22,39" fill="#fff"/></svg>
</section>

<section class="why">
  <h2 class="abs h2">Why choose us</h2>
  <svg class="abs" style="left:60px;top:265px" width="10" height="16" viewBox="0 0 10 16"><polyline points="8,2 2,8 8,14" fill="none" stroke="#333" stroke-width="2"/></svg>
  <svg class="abs" style="right:60px;top:265px" width="10" height="16" viewBox="0 0 10 16"><polyline points="2,2 8,8 2,14" fill="none" stroke="#333" stroke-width="2"/></svg>
  <div class="abs cards">
    <div class="card featured">
      <svg viewBox="0 0 54 46"><rect x="3" y="3" width="48" height="32" fill="none" stroke="#fff" stroke-width="3"/><rect x="22" y="35" width="10" height="6" fill="#fff"/><rect x="15" y="41" width="24" height="3" fill="#fff"/></svg>
      <h3>Managed IT</h3>
      <p>Clients in all industries outsource HLE Technologies for Onsite Server Maintenance and Managed IT Services.</p>
      <span class="more">READ MORE ›</span>
    </div>
    <div class="card">
      <svg viewBox="0 0 54 46"><path d="M14 38 a10 10 0 0 1 0-20 a14 14 0 0 1 26-4 a11 11 0 0 1 2 24z" fill="#33a6d7"/></svg>
      <h3>Private Cloud</h3>
      <p>HLE Technologies provides the design, support and maintenance for quality IT Systems for clients</p>
      <span class="more">READ MORE ›</span>
    </div>
    <div class="card">
      <svg viewBox="0 0 54 46"><ellipse cx="27" cy="8" rx="15" ry="5" fill="#33a6d7"/><rect x="12" y="12" width="30" height="9" rx="4" fill="#33a6d7"/><rect x="12" y="23" width="30" height="9" rx="4" fill="#33a6d7"/><rect x="12" y="34" width="30" height="9" rx="4" fill="#33a6d7"/></svg>
      <h3>Servers</h3>
      <p>HLE Technologies System Design solutions give clients whatever they need to pursue their business.</p>
      <span class="more">READ MORE ›</span>
    </div>
    <div class="card">
      <svg viewBox="0 0 54 46"><circle cx="27" cy="23" r="19" fill="#33a6d7"/><path d="M20 12 q8 4 4 12 q-6 2 -4 10 M32 10 q-2 8 6 10" fill="none" stroke="#fff" stroke-width="2.5"/></svg>
      <h3>Web</h3>
      <p>HLE Technologies provides the design, support and maintenance for quality IT Systems for clients</p>
      <span class="more">READ MORE ›</span>
    </div>
  </div>
</section>

<section class="services">
  <div class="abs devices" role="img" aria-label="Laptop, tablet and phone showing the company brand and growth charts"></div>
  <div class="abs features">
    <div class="feature"><svg viewBox="0 0 32 32"><path d="M2 16 q14-14 28 0 q-14 14 -28 0z" fill="#0292cd"/><circle cx="16" cy="16" r="5" fill="#fff"/></svg><div><h4>Discovery &amp; Strategy</h4><p>Lorem ipsum dolor sit amet, consectetur adipiscing elit do eiusmod tempor.</p></div></div>
    <div class="feature"><svg viewBox="0 0 32 32"><circle cx="10" cy="10" r="5" fill="#0292cd"/><circle cx="22" cy="10" r="5" fill="#0292cd"/><rect x="3" y="17" width="14" height="11" rx="5" fill="#0292cd"/><rect x="15" y="17" width="14" height="11" rx="5" fill="#0292cd"/></svg><div><h4>User Experience Design</h4><p>Lorem ipsum dolor sit amet, consectetur adipiscing elit do eiusmod tempor.</p></div></div>
    <div class="feature"><svg viewBox="0 0 32 32"><rect x="9" y="2" width="14" height="28" rx="2" fill="none" stroke="#0292cd" stroke-width="2.5"/><circle cx="16" cy="25" r="1.6" fill="#0292cd"/></svg><div><h4>Mobile App Development</h4><p>Lorem ipsum dolor sit amet, consectetur adipiscing elit do eiusmod tempor.</p></div></div>
    <div class="feature"><svg viewBox="0 0 32 32"><rect x="3" y="5" width="26" height="17" fill="none" stroke="#0292cd" stroke-width="2.5"/><rect x="1" y="24" width="30" height="3" fill="#0292cd"/></svg><div><h4>Business Application Development</h4><p>Lorem ipsum dolor sit amet, consectetur adipiscing elit do eiusmod tempor.</p></div></div>
  </div>
  <div class="abs stores"><span class="store"></span><span class="store"></span></div>
</section>

<section class="contact">
  <h2 class="abs h2">Contact form</h2>
  <div class="abs form">
    <div class="field" style="left:0;top:0;width:442px">Name *</div>
    <div class="field" style="left:462px;top:0;width:442px">Email *</div>
    <div class="field" style="left:0;top:64px;width:442px">Phone</div>
    <div class="field" style="left:462px;top:64px;width:442px">URL</div>
    <div class="field" style="left:0;top:128px;width:904px;height:120px">Message</div>
  </div>
  <div class="abs send">Send a message</div>
</section>

<section class="blog">
  <h2 class="abs h2">Our blog posts</h2>
  <div class="abs posts">
    <article class="post"><div class="post-img" role="img" aria-label="Office team working at computer screens" style="background:linear-gradient(135deg,#b8cfe0,#3d6d95)"></div><h3>Lorem ipsum dolor</h3><p>Sed ut perspiciatis unde omnis iste natus error sit voluptatem accusantium doloremque.</p><span class="more">READ MORE ›</span></article>
    <article class="post"><div class="post-img" role="img" aria-label="Desk with laptops, papers and coffee seen from above" style="background:linear-gradient(135deg,#d9c2a3,#8a6d52)"></div><h3>Sed quia non numquam</h3><p>Sed ut perspiciatis unde omnis iste natus error sit voluptatem accusantium doloremque.</p><span class="more">READ MORE ›</span></article>
    <article class="post"><div class="post-img" role="img" aria-label="Person working at a laptop in a bright room" style="background:linear-gradient(135deg,#e6e6e6,#7c7c7c)"></div><h3>Eius modi tempora incidunt</h3><p>Sed ut perspiciatis unde omnis iste natus error sit voluptatem accusantium doloremque.</p><span class="more">READ MORE ›</span></article>
  </div>
</section>

<section class="newsletter">
  <h2 class="abs">Sign up to newsletter</h2>
  <p class="abs">Sed ut perspiciatis unde omnis iste natus error sit voluptatem accusantium doloremque laudan</p>
  <div class="abs subscribe"><div class="input">Enter Email</div><div class="go">SUBSCRIBE</div></div>
</section>

<section class="partners">
  <span class="partner"><i></i>Northwind</span>
  <span class="partner">Echofield</span>
  <span class="partner"><i style="border-radius:50%"></i>Tunelane</span>
  <span class="partner"><i></i>Northwind</span>
  <span class="partner">Rydexa</span>
</section>

<footer class="site-footer">
  <div class="abs f-brand"><span class="brand-mark"></span><span class="brand-name">HLE Technologies</span></div>
  <div class="abs socials"><i></i><i></i><i></i><i></i></div>
  <div class="abs col" style="left:405px;width:230px">
    <h4>Quick links</h4>
    <ul><li>Home</li><li>Servers</li><li>Networks</li><li>Managed IT</li><li>Web</li><li>App's</li><li>Internet</li><li>Contact</li></ul>
  </div>
  <div class="abs col" style="left:690px;width:190px">
    <h4>Other links</h4>
    <ul style="columns:1"><li>Terms &amp; Conditions</li><li>Privacy policy</li><li>Information</li><li>Sitemap</li><li>Lorem ipsum dolor</li></ul>
  </div>
  <div class="abs col" style="left:908px;width:200px">
    <h4>Get in touch</h4>
    <ul class="contact-list" style="columns:1">
      <li style="display:flex"><svg viewBox="0 0 18 18"><path d="M9 1a6 6 0 0 1 6 6c0 4-6 10-6 10S3 11 3 7a6 6 0 0 1 6-6z" fill="none" stroke="#ccc" stroke-width="1.6"/><circle cx="9" cy="7" r="2" fill="#ccc"/></svg><span>14 Harlow St, Upper Brookvale</span></li>
      <li style="display:flex"><svg viewBox="0 0 18 18"><path d="M3 2h4l2 4-2 2a10 10 0 0 0 4 4l2-2 4 2v4a1 1 0 0 1-1 1A15 15 0 0 1 2 3a1 1 0 0 1 1-1z" fill="#ccc"/></svg><span>Phone : 1300 555 014</span></li>
      <li style="display:flex"><svg viewBox="0 0 18 18"><rect x="1" y="4" width="16" height="11" fill="none" stroke="#ccc" stroke-width="1.6"/><polyline points="1,4 9,10 17,4" fill="none" stroke="#ccc" stroke-width="1.6"/></svg><span>Email : info@hle.com.au</span></li>
    </ul>
  </div>
  <p class="abs copy">Copyright © HLE Technologies, 2017. All rights reserved &nbsp;|&nbsp; Privacy policy</p>
</footer>

</body>
</html>
```